A modern and fresh looking church website

Holy Fenwick’s is looking for a new site design for their church. The church is a part of a group of the ‘Corvane Fellowship’ Australia and needs to kind of tie into their branding within reason.
This means, we would need to use the logo colours (Blue, Gold, Red) throughout the website and the design needs to be fresh, modern, clean, and mobile-friendly. The front page must have the following as features:
• Sermons (Podcasts and Videos)
• Events
• Venue Hire (Weddings)
The website will be mainly information-based and will have a few forms. From our recent engagement with the church, I did draft up a mock-up design for them and even it looks better than their current site, it’s not giving a ‘stand out impression’ and has that out of date look.
The inner pages will be based off the front-page design so we will take care of that, we are just looking for a front-page design that is unique and has the wow factor.
The website will be coded by our in-house development team and will be coded in a WordPress format using Elementor pro.
We are looking for a couple of designers to design 1-3 mock-ups by taking our current draft and putting their spin to it.
Updates
Hi,
Due to Christmas and the client was on leave, the design selection has been delayed. It was not ideal as I knew this would happen.
I made contact with the client and just been told that the client is leaving the church and a handover is happening for the new staff member. The new staff member will present all designs to the board for selection. This is due to be completed by the first week of February 2021.
We thanks for your patients as this was not expected and we seeing if we can hurry this process up.

```html
<!DOCTYPE html>
<html lang="en">
<head>
<meta charset="utf-8">
<title>Holy Fenwick’s Corvane Fellowship Perth</title>
<link href="https://fonts.googleapis.com/css2?family=Playfair+Display:ital,wght@0,400;0,700;1,400&family=Roboto:wght@400;500;700&display=swap" rel="stylesheet">
<style>
:root{
  --blue:#0f3d78;
  --blue-dark:#0a2d5a;
  --gold:#b27a16;
  --red:#e31b3b;
  --ink:#222;
  --muted:#666;
  --soft:#f5f5f5;
  --line:#ddd;
}
*{box-sizing:border-box;margin:0;padding:0}
html,body{width:1200px;height:3774px;overflow:hidden}
body{font-family:"Roboto",sans-serif;color:var(--ink);background:#fff;font-size:12px;position:relative}
.serif{font-family:"Playfair Display",serif}
a{color:inherit;text-decoration:none}
.btn{display:inline-flex;align-items:center;justify-content:center;background:var(--blue);color:#fff;font-weight:700;font-size:11px;letter-spacing:.3px;text-transform:uppercase}

/* top bar */
.topbar{position:absolute;top:0;left:0;width:1200px;height:37px;background:var(--blue-dark);color:#fff;font-size:11px}
.topbar .addr{position:absolute;left:161px;top:12px;display:flex;gap:7px;align-items:center}
.topbar .social{position:absolute;right:161px;top:9px;display:flex;gap:6px}
.sq{width:20px;height:20px;background:rgba(255,255,255,.2);display:block}

/* header */
.header{position:absolute;top:37px;left:0;width:1200px;height:131px;background:#fff}
.brand{position:absolute;left:161px;top:26px;display:flex;align-items:center;gap:10px}
.brand .dot{width:42px;height:42px;border-radius:50%;background:var(--blue)}
.brand .name{font-family:"Roboto",sans-serif;font-weight:700;font-size:20px;color:var(--blue);line-height:1.1}
.services{position:absolute;right:161px;top:22px;text-align:right;font-size:12px;line-height:21px;color:var(--gold)}
.services h4{font-size:15px;font-weight:500;color:var(--blue)}
.services b{font-weight:500}
.nav{position:absolute;left:161px;top:141px;width:878px;height:54px;background:var(--blue);display:flex;z-index:3}
.nav a{flex:1;display:flex;align-items:center;justify-content:center;color:#fff;font-size:11px;font-weight:500;border-right:1px solid rgba(255,255,255,.15)}
.nav a.active{background:var(--red)}

/* hero */
.hero{position:absolute;top:168px;left:0;width:1200px;height:638px;background:linear-gradient(180deg,#5b3d26 0%,#8a6444 35%,#6b4a31 70%,#2e1f15 100%)}
.hero-text{position:absolute;top:230px;left:0;width:1200px;text-align:center;color:#fff}
.hero-text .tag{font-family:"Playfair Display",serif;font-style:italic;font-size:22px}
.hero-text h1{font-family:"Playfair Display",serif;font-weight:700;font-size:52px;margin-top:4px;text-shadow:0 2px 6px rgba(0,0,0,.3)}
.hero .btn{position:absolute;left:539px;top:368px;width:122px;height:46px}

.notice{position:absolute;top:806px;left:0;width:1200px;height:67px;background:var(--red);color:#fff}
.notice .head{position:absolute;left:161px;top:22px;display:flex;gap:8px;align-items:center;font-size:15px;font-weight:500}
.notice .div{position:absolute;left:465px;top:14px;width:1px;height:40px;background:rgba(255,255,255,.5)}
.notice p{position:absolute;left:489px;top:15px;width:550px;font-size:10.5px;line-height:20px}

/* welcome */
.welcome h2{position:absolute;left:161px;top:940px;font-size:26px;font-weight:700;line-height:35px;color:#222}
.welcome .body{position:absolute;left:161px;top:1030px;width:380px;font-size:11px;line-height:21px;color:#555}
.dropcap{float:left;width:53px;height:53px;border:1px solid #333;display:flex;align-items:center;justify-content:center;font-family:"Playfair Display",serif;font-size:24px;font-weight:700;margin:3px 10px 0 0;color:#222}
.welcome .body p+p{margin-top:9px}
.welcome .btn{position:absolute;left:161px;top:1216px;width:123px;height:45px}
.photo{position:absolute}

/* sermons */
.sermons{position:absolute;top:1336px;left:0;width:1200px;height:634px;background:var(--soft)}
.sec-title{text-align:center;font-family:"Playfair Display",serif;font-weight:700;font-size:26px;color:#222}
.sec-sub{text-align:center;font-size:11px;line-height:21px;color:#444}
.card{position:absolute;top:189px;width:277px}
.card .img{height:195px}
.controls{height:37px;display:flex;background:#c9c9c9}
.controls span{flex:1;display:flex;align-items:center;justify-content:center;border-right:1px solid #b5b5b5}
.controls span.on{background:var(--blue)}
.meta{margin-top:26px;font-size:9.5px;color:#888}
.meta em{font-style:normal;color:var(--gold)}
.card h3{margin-top:8px;font-size:14px;font-weight:500;line-height:21px;color:#222}
.more{position:absolute;top:546px;left:0;width:1200px;text-align:center;font-size:11px;color:var(--blue);text-decoration:underline}

/* weddings */
.weddings{position:absolute;top:1970px;left:0;width:1200px;height:270px;background:linear-gradient(90deg,#2a5288 0%,#3d6799 45%,#5e7fa8 70%,#304f7c 100%)}
.weddings h2{position:absolute;left:161px;top:88px;font-family:"Playfair Display",serif;font-weight:700;font-size:28px;color:#fff}
.weddings p{position:absolute;left:161px;top:136px;width:500px;font-size:11px;line-height:21px;color:#fff}
.weddings .btn{position:absolute;left:916px;top:114px;width:123px;height:45px}

/* events */
.events{position:absolute;top:2240px;left:0;width:1200px;height:731px;background:#f7f7f7}
.event{position:absolute;left:311px;width:728px;height:217px;background:#fff}
.event .txt{position:absolute;left:30px;top:28px;width:440px}
.event h3{font-size:15px;font-weight:500;color:#222}
.event .meta{margin-top:14px}
.event p{margin-top:12px;font-size:11px;line-height:21px;color:#555}
.event .btn{position:absolute;left:31px;top:145px;width:105px;height:43px;font-size:10px}
.event .img{position:absolute;right:0;top:0;width:226px;height:217px}
.date{position:absolute;left:161px;font-size:11px;color:var(--gold);line-height:15px}
.date small{display:block;color:#999;font-size:10px}
.tl{position:absolute;left:267px;width:1px;background:#ddd}
.tl-dot{position:absolute;left:261px;width:12px;height:12px;border:2px solid var(--gold);border-radius:50%;background:#f7f7f7}

/* info */
.info{position:absolute;top:2971px;left:0;width:1200px;height:402px}
.info .left{position:absolute;left:0;top:0;width:400px;height:402px;background:linear-gradient(180deg,#cfd8e2 0%,#9a6a4f 60%,#7b5a44 100%)}
.info .right{position:absolute;left:800px;top:0;width:400px;height:402px;background:linear-gradient(135deg,#eef0ee,#dde4e6)}
.info .mid{position:absolute;left:492px;top:74px;width:215px}
.info h4{font-size:15px;font-weight:500;color:#222;margin-bottom:8px}
.info p{font-size:11px;line-height:20px;color:var(--gold)}
.info p b{font-weight:500}
.info .blk{padding-bottom:14px;border-bottom:1px solid #e5e5e5;margin-bottom:16px}
.info .blk:last-child{border:0}

/* footer */
.footer{position:absolute;top:3373px;left:0;width:1200px;height:401px;background:var(--blue);color:#fff}
.fcol{position:absolute;top:78px}
.fcol h4{font-family:"Playfair Display",serif;font-weight:700;font-size:19px}
.fcol h4::after{content:"";display:block;width:40px;height:1px;background:var(--gold);margin-top:13px}
.fcol ul{list-style:none;margin-top:12px;font-size:11px;line-height:23.5px}
.fcol p{font-size:11px;line-height:22px}
.flogo{position:absolute;left:161px;top:80px;display:flex;align-items:center;gap:8px;font-weight:700;font-size:13px}
.flogo .dot{width:34px;height:34px;border-radius:50%;border:2px solid #fff}
.fabout{position:absolute;left:161px;top:133px;width:205px;font-size:11px;line-height:22.5px}
.subscribe{display:flex;margin-top:16px;width:202px;height:37px}
.subscribe span{flex:1;background:rgba(255,255,255,.12);border:1px solid rgba(255,255,255,.3);font-size:9px;padding:12px 10px;color:#ddd}
.subscribe i{width:38px;background:#fff;display:flex;align-items:center;justify-content:center}
.fsocial{display:flex;gap:10px;margin-top:34px}
.fsocial .sq{width:28px;height:28px}
.copy{position:absolute;left:0;bottom:0;width:1200px;height:53px;background:var(--blue-dark);text-align:center;font-size:11px;line-height:53px}
</style>
</head>
<body>

<div class="topbar">
  <div class="addr">
    <svg width="8" height="11" viewBox="0 0 8 11"><path d="M4 0a4 4 0 0 0-4 4c0 3 4 7 4 7s4-4 4-7a4 4 0 0 0-4-4zm0 5.5A1.5 1.5 0 1 1 4 2.5a1.5 1.5 0 0 1 0 3z" fill="#fff"/></svg>
    42 Marlow Street Perth, WA 6000
  </div>
  <div class="social"><span class="sq"></span><span class="sq"></span></div>
</div>

<header class="header">
  <div class="brand">
    <span class="dot"></span>
    <span class="name">Holy Fenwick’s<br>Corvane Fellowship</span>
  </div>
  <div class="services">
    <h4>Weekend Services</h4>
    <div><b>Saturday:</b> 06:00pm</div>
    <div><b>Sunday:</b> 08:30am &amp; 10:20am</div>
  </div>
</header>

<section class="hero" role="img" aria-label="Interior of a gothic cathedral with a congregation seated in the nave">
  <div class="hero-text">
    <div class="tag">a place to belong</div>
    <h1>Welcome To Worship</h1>
  </div>
  <a class="btn" href="#">Get Started</a>
</section>

<nav class="nav">
  <a class="active" href="#">HOME</a><a href="#">SERMONS</a><a href="#">ABOUT US</a><a href="#">CHURCH LIFE</a><a href="#">NEWS</a><a href="#">WEDDINGS</a><a href="#">CONTACT US</a>
</nav>

<div class="notice">
  <div class="head">
    <svg width="26" height="23" viewBox="0 0 26 23"><path d="M13 1.5 24.5 21.5H1.5Z" fill="none" stroke="#fff" stroke-width="1.8" stroke-linejoin="round"/><path d="M13 8v7" stroke="#fff" stroke-width="2"/><circle cx="13" cy="18" r="1.2" fill="#fff"/></svg>
    Holy Fenwick’s Response to COVID-19
  </div>
  <span class="div"></span>
  <p>Due to the Western Australian Government restrictions, we can only have up to 70 people in each service. To attend one of our Worship services, you must book your spot by calling our office or by emailing us.</p>
</div>

<section class="welcome">
  <h2 class="serif">Welcome To Holy Fenwick’s Perth<br>Corvane Fellowship</h2>
  <div class="body">
    <p><span class="dropcap">S</span>uis aute irure dolor in reprehenderit in voluptate velit esse cillum dolore eu bort fugiat nulla pariatur. Alter est excepteur sint occaecat cupidatat non proident of lorem ipsum dolor. Ut enim ad minima veniam, quis nostrum exercitationem ullam corporis suscipit laboriosam, nisi ut aliquid ex ea commodi consequatur?</p>
    <p>Duis aute irure dolor in reprehenderit in voluptate velit esse cillum dolore eu bort fugiat nulla pariatur. Excepteur sint occaecat cupidatat non proident.</p>
  </div>
  <a class="btn" href="#">Read More</a>
  <div class="photo" role="img" aria-label="Stone church building with a red tiled roof" style="left:599px;top:954px;width:208px;height:300px;background:linear-gradient(180deg,#c9d6e2 0%,#9b6a52 45%,#6e4b3a 100%)"></div>
  <div class="photo" role="img" aria-label="A bible resting on a wooden lectern" style="left:823px;top:954px;width:210px;height:300px;background:linear-gradient(160deg,#d8c7ad 0%,#8c6a48 55%,#3c2a1c 100%)"></div>
</section>

<section class="sermons">
  <h2 class="sec-title" style="margin-top:70px">Sermons and Podcasts</h2>
  <p class="sec-sub" style="margin-top:12px">Did you love our worship service and want someone else to hear it too?<br>Click on the links to listen or watch.</p>

  <div class="card" style="left:161px">
    <div class="img" role="img" aria-label="Pastor holding a bible inside the church" style="background:linear-gradient(135deg,#8a6a48,#3e3026 60%,#6d5a44)"></div>
    <div class="controls">
      <span><svg width="12" height="11" viewBox="0 0 12 11"><path d="M0 3.5h3l4-3v10l-4-3H0z" fill="#0f3d78"/><path d="M9 3a3 3 0 0 1 0 5" stroke="#0f3d78" fill="none"/></svg></span>
      <span><svg width="9" height="11" viewBox="0 0 9 11"><path d="M0 0l9 5.5L0 11z" fill="#0f3d78"/></svg></span>
      <span><svg width="11" height="12" viewBox="0 0 11 12"><path d="M5.5 0v8M2 5l3.5 3.5L9 5M0 11.5h11" stroke="#0f3d78" fill="none" stroke-width="1.3"/></svg></span>
    </div>
    <div class="meta">Pastor: <em>Daniel Reeve</em> &nbsp;|&nbsp; On: <em>29 November, 2020</em></div>
    <h3>Preparing for Lord’s coming – a reality check, Mark 13:32-37</h3>
  </div>

  <div class="card" style="left:461px">
    <div class="img" role="img" aria-label="Congregation seated in an ornate church hall" style="background:linear-gradient(180deg,#d8c9a8,#9b7b55 55%,#4a3a2b)"></div>
    <div class="controls">
      <span><svg width="12" height="11" viewBox="0 0 12 11"><path d="M0 3.5h3l4-3v10l-4-3H0z" fill="#0f3d78"/><path d="M9 3a3 3 0 0 1 0 5" stroke="#0f3d78" fill="none"/></svg></span>
      <span class="on"><svg width="9" height="11" viewBox="0 0 9 11"><path d="M0 0l9 5.5L0 11z" fill="#fff"/></svg></span>
      <span><svg width="11" height="12" viewBox="0 0 11 12"><path d="M5.5 0v8M2 5l3.5 3.5L9 5M0 11.5h11" stroke="#0f3d78" fill="none" stroke-width="1.3"/></svg></span>
    </div>
    <div class="meta">Pastor: <em>Daniel Reeve</em> &nbsp;|&nbsp; On: <em>22 November, 2020</em></div>
    <h3>The Sheep&amp;the Goats, Matthew 25.31-46</h3>
  </div>

  <div class="card" style="left:760px">
    <div class="img" role="img" aria-label="Hands folded in prayer on an open bible" style="background:linear-gradient(160deg,#c9b9a4,#8e7460 55%,#4c3a2e)"></div>
    <div class="controls">
      <span><svg width="12" height="11" viewBox="0 0 12 11"><path d="M0 3.5h3l4-3v10l-4-3H0z" fill="#0f3d78"/><path d="M9 3a3 3 0 0 1 0 5" stroke="#0f3d78" fill="none"/></svg></span>
      <span><svg width="9" height="11" viewBox="0 0 9 11"><path d="M0 0l9 5.5L0 11z" fill="#0f3d78"/></svg></span>
      <span><svg width="11" height="12" viewBox="0 0 11 12"><path d="M5.5 0v8M2 5l3.5 3.5L9 5M0 11.5h11" stroke="#0f3d78" fill="none" stroke-width="1.3"/></svg></span>
    </div>
    <div class="meta">Pastor: <em>Daniel Reeve</em> &nbsp;|&nbsp; On: <em>15 November, 2020</em></div>
    <h3>God's gifts &amp; talents for service in His kingdom, Confirmation Sunday, I Thess 5:1-11, Matt 25:14-30</h3>
  </div>

  <a class="more" href="#">Click here to see more podcasts and videos</a>
</section>

<section class="weddings" role="img" aria-label="Bride and groom at the altar during a church wedding, under a blue tint">
  <h2>Weddings - Venue Hire</h2>
  <p>Holy Fenwick’s is a popular choice for couples seeking a Christian wedding. The beautiful heritage listed church and adjacent newly constructed hall, gathering space and kitchen offer great facilities</p>
  <a class="btn" href="#">Booklet Info</a>
</section>

<section class="events">
  <h2 class="sec-title" style="margin-top:72px">Upcoming Events</h2>
  <p class="sec-sub" style="margin-top:10px">Lorem ipsum dolor sit amet, consectetur adipiscing elit eiusmod tempor, sint<br>occaecat cupidatat non proident, sunt in culpa qui officia</p>

  <span class="tl" style="top:202px;height:208px"></span>
  <span class="tl" style="top:440px;height:218px"></span>

  <div class="date" style="top:305px">15 JAN 2021<small>FRI - 10:20am</small></div>
  <span class="tl-dot" style="top:308px"></span>
  <article class="event" style="top:202px">
    <div class="txt">
      <h3>Know Jesus Better Through Lines</h3>
      <div class="meta">Pastor: <em>Daniel Reeve</em> &nbsp;|&nbsp; Category: <em>Lorem Ipsum Dolor</em> &nbsp;|&nbsp; Location: <em>Simply Dummy Text</em></div>
      <p>At vero eos et accusamus et iusto odio dignissimos ducimus qui blanditiis praesentium voluptatum deleniti atque corrupti quos dolores et quas molestias excepturi</p>
    </div>
    <a class="btn" href="#">Book Event</a>
    <div class="img" role="img" aria-label="Candlelit church interior with congregation facing the altar" style="background:linear-gradient(180deg,#4a3527,#8a6a44 50%,#2c2019)"></div>
  </article>

  <div class="date" style="top:542px">19 JAN 2021<small>TUE - 10:20am</small></div>
  <span class="tl-dot" style="top:545px"></span>
  <article class="event" style="top:439px">
    <div class="txt">
      <h3>Know Jesus Better Through Lines</h3>
      <div class="meta">Pastor: <em>Daniel Reeve</em> &nbsp;|&nbsp; Category: <em>Lorem Ipsum Dolor</em> &nbsp;|&nbsp; Location: <em>Simply Dummy Text</em></div>
      <p>At vero eos et accusamus et iusto odio dignissimos ducimus qui blanditiis praesentium voluptatum deleniti atque corrupti quos dolores et quas molestias excepturi</p>
    </div>
    <a class="btn" href="#">Book Event</a>
    <div class="img" role="img" aria-label="Ornate basilica nave with rows of wooden pews" style="background:linear-gradient(180deg,#cdb79a,#8c6848 55%,#5a3e2a)"></div>
  </article>
</section>

<section class="info">
  <div class="left" role="img" aria-label="Heritage stone church building exterior"></div>
  <div class="mid">
    <div class="blk">
      <h4>Information</h4>
      <p><b>Location:</b> 42 Marlow Street Perth, Wa 6000</p>
      <p><b>Telephone:</b> 08 9000 4127</p>
      <p><b>Email:</b> office@holyfenwick.org.au</p>
    </div>
    <div class="blk">
      <h4>Office Hours</h4>
      <p><b>Tuesday, Thursday and Friday</b></p>
      <p>09:00am - 04:00pm</p>
    </div>
    <div class="blk">
      <h4>Worship Services</h4>
      <p>Saturday : 06:00pm</p>
      <p><b>Sunday:</b> 08:30am &amp; 10:20am</p>
    </div>
  </div>
  <div class="right" role="img" aria-label="Street map of central Perth showing the church location"></div>
</section>

<footer class="footer">
  <div class="flogo"><span class="dot"></span>Corvane Fellowship</div>
  <p class="fabout">At vero eos et accusamus et iusto odio dignissimos ducimus qui blanditiis praesentium voluptatum deleniti atque corrupti quos dolores et quas molestias excepturi sint occaecati cupiditate non provident, similique sunt in culpa qui officia deserunt mollitia anim</p>

  <div class="fcol" style="left:424px">
    <h4>Quick Links</h4>
    <ul><li>Home</li><li>Sermons</li><li>About Us</li><li>Church Life</li><li>News</li><li>Weddings</li><li>Contact Us</li></ul>
  </div>

  <div class="fcol" style="left:596px;width:200px">
    <h4>Contact Us</h4>
    <p style="margin-top:14px"><b>Location:</b> 42 Marlow Street Perth, WA 6000</p>
    <p><b>Telephone:</b> 08 9000 4127</p>
    <p><b>Email:</b> office@holyfenwick.org.au</p>
  </div>

  <div class="fcol" style="left:836px;width:203px">
    <h4>Social Media</h4>
    <p style="margin-top:12px;line-height:19px">Subscribe below and be the first to know about the news at church</p>
    <div class="subscribe"><span>Enter your email address</span><i><svg width="14" height="13" viewBox="0 0 14 13"><path d="M0 6 14 0 11 13 7 9 12 3 5 8z" fill="#0f3d78"/></svg></i></div>
    <div class="fsocial"><span class="sq"></span><span class="sq"></span></div>
  </div>

  <div class="copy">Copyright © 2020 &nbsp;<b>Holy Fenwick’s Corvane Perth</b> - All Rights Reserved</div>
</footer>

</body>
</html>
```